Park furniture company needs a new product flyer

We're a street and park furniture supply company and we have a new range of furniture that we would like to showcase to prospective customers.
Pictures, logo and copy attached.
Furniture pictures are also available with a black background.
Warranty information needs to feature on the flyer.
Recycled content information needs to feature on the flyer.

Target Market(s)

Landscape Architects

Font styles to use
Serif

Requirements
Must have
• Professional fonts and graphics.
Should not have
• comic sans or similar fonts - cheap graphics

```html
<!DOCTYPE html>
<html lang="en">
<head>
<meta charset="utf-8">
<title>Linden Yard – Product Flyer</title>
<link rel="stylesheet" href="https://fonts.googleapis.com/css2?family=Montserrat:wght@600;700;800&family=Raleway:wght@400;500&display=swap">
<style>
  :root {
    --paper: #e8e8ea;
    --blue: #0b5fb3;
    --ink: #3c3c3e;
    --text: #2a2a2c;
    --disc: #dcdcdf;
    --black: #151515;
  }
  * { box-sizing: border-box; margin: 0; padding: 0; }
  html, body { width: 1070px; height: 1200px; overflow: hidden; }
  body { background: var(--paper); font-family: "Raleway", Arial, sans-serif; color: var(--text); }
  .flyer { position: relative; width: 1070px; height: 1200px; overflow: hidden; background: var(--paper); }

  .edge-bar { position: absolute; left: 0; top: 0; width: 25px; height: 688px; background: var(--blue); }
  .backdrop { position: absolute; inset: 0; }

  .brand { position: absolute; left: 0; right: 0; top: 78px; text-align: center; }
  .brand-name { font-family: "Montserrat", Arial, sans-serif; font-weight: 700; font-size: 62px; letter-spacing: 2px; color: var(--ink); line-height: 1; }
  .brand-mark { display: inline-block; width: 14px; height: 14px; background: var(--blue); margin-left: 10px; vertical-align: 6px; }

  .stat { position: absolute; left: 101px; top: 250px; }
  .stat-figure { font-family: "Montserrat", Arial, sans-serif; font-weight: 800; font-size: 112px; line-height: 1; color: var(--blue); letter-spacing: -3px; }
  .stat-label { font-family: "Montserrat", Arial, sans-serif; font-weight: 600; font-size: 18px; color: var(--ink); margin-top: 4px; margin-left: 3px; }

  .product-photo { position: absolute; border-radius: 6px; }
  .photo-table { left: 100px; top: 410px; width: 450px; height: 300px; background: linear-gradient(160deg, #5d4a3c 0%, #3e3129 45%, #b5aa9a 100%); }
  .photo-bench { left: 560px; top: 668px; width: 430px; height: 490px; background: linear-gradient(165deg, #8a4a22 0%, #b3622e 50%, #8f8575 100%); }

  .features { position: absolute; list-style: none; }
  .feature { display: flex; align-items: flex-start; }
  .feature-num { font-family: "Montserrat", Arial, sans-serif; font-weight: 700; font-size: 46px; line-height: 1; color: var(--blue); width: 44px; }
  .feature-text { font-size: 14px; line-height: 16.5px; }

  .features-top { left: 662px; top: 0; }
  .features-top .feature { position: absolute; left: 0; width: 320px; }
  .features-top .feature-num { margin-top: 4px; }
  .features-top .feature-text { width: 270px; }

  .features-bottom { left: 0; top: 0; }
  .features-bottom .feature { position: absolute; left: 120px; width: 330px; flex-direction: row-reverse; text-align: right; }
  .features-bottom .feature-num { text-align: center; width: 60px; margin-left: 8px; }
  .features-bottom .feature-text { width: 262px; }

  .warranty { position: absolute; right: 96px; top: 590px; text-align: right; }
  .warranty-figure { font-family: "Montserrat", Arial, sans-serif; font-weight: 800; font-size: 82px; line-height: 1; color: var(--blue); letter-spacing: -2px; }
  .warranty-label { font-family: "Montserrat", Arial, sans-serif; font-weight: 600; font-size: 25px; color: var(--ink); margin-top: -4px; }

  .web { position: absolute; left: 83px; top: 1123px; width: 355px; height: 29px; background: var(--black); color: #fff; font-family: "Montserrat", Arial, sans-serif; font-weight: 600; font-size: 16px; letter-spacing: 2px; text-align: center; line-height: 29px; }
</style>
</head>
<body>
<main class="flyer">
  <svg class="backdrop" width="1070" height="1200" viewBox="0 0 1070 1200" aria-hidden="true">
    <circle cx="287" cy="472" r="272" fill="var(--disc)"/>
    <circle cx="860" cy="1010" r="280" fill="var(--blue)"/>
  </svg>
  <div class="edge-bar"></div>

  <header class="brand">
    <span class="brand-name">LINDEN YARD</span><span class="brand-mark"></span>
  </header>

  <section class="stat">
    <div class="stat-figure">98%</div>
    <div class="stat-label">Recycled Composite Battens</div>
  </section>

  <div class="product-photo photo-table" role="img" aria-label="Product photo: picnic table with two benches, dark composite battens on aluminium frames"></div>

  <ol class="features features-top">
    <li class="feature" style="top:252px"><span class="feature-num">1</span><p class="feature-text">European inspired with a unique and original design, that is functional all while respecting the environment.</p></li>
    <li class="feature" style="top:329px"><span class="feature-num">2</span><p class="feature-text">Our range is designed to make life easier for people; created using extremely durable, ultra low maintenance materials.</p></li>
    <li class="feature" style="top:417px"><span class="feature-num">3</span><p class="feature-text">Featuring 98% recycled composite battens in a range of stain and fade-resistant colour options and a unique aluminium frame design.</p></li>
    <li class="feature" style="top:507px"><span class="feature-num">4</span><p class="feature-text">The capped composite battens come with a 10-year commercial warranty covering staining, fading and structural performance.</p></li>
  </ol>

  <section class="warranty">
    <div class="warranty-figure">10-Years</div>
    <div class="warranty-label">warranty</div>
  </section>

  <div class="product-photo photo-bench" role="img" aria-label="Product photo: bench seat with backrest and armrests, warm timber-tone battens on aluminium frame"></div>

  <ol class="features features-bottom">
    <li class="feature" style="top:798px"><span class="feature-num">5</span><p class="feature-text">Site-specific for healthcare applications offering wheelchair accessibility options</p></li>
    <li class="feature" style="top:879px"><span class="feature-num">6</span><p class="feature-text">The Linden Yard range comprises of a seat with optional armrests, bench seat and table, available in both standard or DDA designs.</p></li>
    <li class="feature" style="top:974px"><span class="feature-num">7</span><p class="feature-text">Uniform length of 1800mm with tailored options available.</p></li>
    <li class="feature" style="top:1040px"><span class="feature-num">8</span><p class="feature-text" style="margin-top:12px">Bolt down or freestanding options.</p></li>
  </ol>

  <div class="web">WWW.LINDENYARD.COM</div>
</main>
</body>
</html>
```